Email Marketing Campaign Templates

Email drip childcare campaign designed to communicate with parents interested in services. We would like the template(s) to be created so that we can change the content as needed.I will add below collateral that we have used in the past as well as logo.
three to for templates 1.) welcome template 2/ things to bring 3) generic template
Target Market(s)
Parents and Millennials
Industry/Entity Type
Childcare
Colors
85cae6
0493ce
9bcb3c
add136
fefefe
faa54b
cadf82
86cae7
33a6d7
Requirements
Must have
- Photos of staff with children
Nice to have
- Photos

```html
<!DOCTYPE html>
<html lang="en">
<head>
<meta charset="utf-8">
<title>Seedling Early Learning Center – Welcome</title>
<link rel="stylesheet" href="https://fonts.googleapis.com/css2?family=Courgette&family=Tinos&family=Open+Sans:ital,wght@1,700&display=swap">
<style>
  :root {
    --green: #73bf45;
    --green-soft: #7fc653;
    --blue: #0a6fc2;
    --blue-light: #33a6d7;
    --orange: #f9b233;
    --white: #fefefe;
  }
  * { margin: 0; padding: 0; box-sizing: border-box; }
  html, body { width: 1200px; height: 3005px; overflow: hidden; }
  body {
    position: relative;
    background: radial-gradient(circle at 20% 40%, var(--green-soft), var(--green) 60%);
    font-family: "Tinos", "Times New Roman", serif;
    color: var(--white);
  }

  .hero-photo {
    position: absolute; left: 0; top: 0; width: 1200px; height: 1130px;
    background:
      radial-gradient(ellipse 230px 420px at 330px 520px, rgba(120,122,130,.55), rgba(120,122,130,0) 100%),
      radial-gradient(ellipse 260px 90px at 400px 900px, rgba(240,170,40,.55), rgba(240,170,40,0) 100%),
      linear-gradient(175deg, rgba(0,0,0,0) 48%, rgba(232,120,70,.45) 58%, rgba(90,150,200,.35) 66%, rgba(0,0,0,0) 74%),
      linear-gradient(100deg, #c8cf3e 0%, #b9c454 10%, #e7e4dc 28%, #efeef0 60%, #f6f7f9 100%);
  }
  .hero-wave { position: absolute; left: 0; top: 960px; width: 1200px; height: 180px; }

  .brand {
    position: absolute; left: 750px; top: 150px; width: 400px;
    display: flex; align-items: center; gap: 18px;
    font-family: "Courgette", cursive; color: var(--blue-light);
  }
  .brand-dot { width: 64px; height: 64px; border-radius: 50%; background: var(--green); flex: none; }
  .brand-name { font-size: 44px; line-height: 1.15; font-weight: 400; }

  .welcome-title {
    position: absolute; left: 0; top: 1162px; width: 1200px; text-align: center;
    font-family: "Courgette", cursive; font-weight: 400; font-size: 54px; line-height: 72px;
  }
  .welcome-copy {
    position: absolute; left: 0; top: 1318px; width: 1200px; text-align: center;
    font-size: 29px; line-height: 46px; white-space: nowrap;
  }
  .read-more {
    position: absolute; left: 420px; top: 1482px; width: 330px; height: 90px;
    background: var(--orange); color: var(--white);
    font-family: "Open Sans", sans-serif; font-style: italic; font-weight: 700; font-size: 28px;
    display: flex; align-items: center; justify-content: center;
  }

  .card { position: absolute; width: 540px; text-align: center; }
  .card-photo {
    width: 502px; height: 326px; margin: 0 auto;
    border: 6px solid var(--white);
    box-shadow: 0 4px 10px rgba(0,0,0,.12);
  }
  .card-title { font-family: "Courgette", cursive; font-weight: 400; font-size: 46px; line-height: 60px; margin-top: 22px; }
  .card-copy { font-size: 27px; line-height: 39px; margin-top: 2px; white-space: nowrap; }
  .card.left  { left: 50px; }
  .card.right { left: 646px; }
  .card.row1 { top: 1644px; }
  .card.row2 { top: 2232px; }

  .photo-teacher { background: linear-gradient(120deg, #7a4a2e 0%, #c98f6b 30%, #3a7fc4 50%, #e8d9c4 70%, #f3efe9 100%); }
  .photo-snack   { background: linear-gradient(110deg, #e9d6b8 0%, #d33b3b 30%, #f0d8c0 50%, #2d2a3a 75%, #cfd6de 100%); }
  .photo-table   { background: linear-gradient(160deg, #5a4a3a 0%, #b9865a 30%, #3b6fb0 55%, #4f9a6a 70%, #c9a47a 100%); }
  .photo-paint   { background: linear-gradient(130deg, #f2f0ea 0%, #f6c64a 30%, #e56b3b 50%, #7cc0e8 70%, #f1eee8 100%); }

  .footer { position: absolute; left: 0; top: 2790px; width: 1200px; height: 215px; }
  .copyright {
    position: absolute; left: 0; top: 2918px; width: 1200px; text-align: center;
    font-size: 32px; letter-spacing: 1px;
  }
</style>
</head>
<body>
  <div class="hero-photo" role="img" aria-label="Photo of a toddler playing with toy cars on a colourful classroom rug"></div>
  <svg class="hero-wave" viewBox="0 0 1200 180" preserveAspectRatio="none" aria-hidden="true">
    <path d="M0 165 C200 140 420 30 660 40 C800 50 880 125 960 120 C1060 115 1120 40 1200 50 V180 H0 Z" fill="var(--green)"/>
  </svg>

  <div class="brand">
    <span class="brand-dot"></span>
    <span class="brand-name">Seedling<br>Early Learning Center</span>
  </div>

  <h1 class="welcome-title">Welcome to our children&nbsp; at<br>seedling early learning center</h1>
  <p class="welcome-copy">Lorem Ipsum is simply dummy text of the printing and typesetting in-<br>dustry. Lorem Ipsum has been the industry's standard dummy text ever<br>since the 1500s, when an unknown printer took a galley</p>
  <div class="read-more">Read More..</div>

  <div class="card left row1">
    <div class="card-photo photo-teacher" role="img" aria-label="Photo of a teacher showing a tablet to a young child"></div>
    <h2 class="card-title">Children Text here</h2>
    <p class="card-copy">Lorem Ipsum is simply dummy text of<br>the printing and typesetting industry.<br>Lorem Ipsum has been</p>
  </div>
  <div class="card right row1">
    <div class="card-photo photo-snack" role="img" aria-label="Photo of two children enjoying a snack"></div>
    <h2 class="card-title">Children Text here</h2>
    <p class="card-copy">Lorem Ipsum is simply dummy text of<br>the printing and typesetting industry.<br>Lorem Ipsum has been</p>
  </div>
  <div class="card left row2">
    <div class="card-photo photo-table" role="img" aria-label="Photo of children working together at a classroom table"></div>
    <h2 class="card-title">Children Text here</h2>
    <p class="card-copy">Lorem Ipsum is simply dummy text of<br>the printing and typesetting industry.<br>Lorem Ipsum has been</p>
  </div>
  <div class="card right row2">
    <div class="card-photo photo-paint" role="img" aria-label="Photo of children with paint-covered hands"></div>
    <h2 class="card-title">Children Text here</h2>
    <p class="card-copy">Lorem Ipsum is simply dummy text of<br>the printing and typesetting industry.<br>Lorem Ipsum has been</p>
  </div>

  <svg class="footer" viewBox="0 0 1200 215" preserveAspectRatio="none" aria-hidden="true">
    <g fill="var(--blue)">
      <circle cx="40" cy="70" r="45"/><circle cx="140" cy="60" r="50"/><circle cx="250" cy="75" r="45"/>
      <circle cx="360" cy="62" r="52"/><circle cx="470" cy="76" r="44"/><circle cx="580" cy="60" r="52"/>
      <circle cx="690" cy="74" r="46"/><circle cx="800" cy="62" r="50"/><circle cx="910" cy="76" r="44"/>
      <circle cx="1020" cy="60" r="52"/><circle cx="1130" cy="72" r="48"/><circle cx="1200" cy="66" r="40"/>
      <rect x="0" y="70" width="1200" height="145"/>
    </g>
  </svg>
  <p class="copyright">Copyright@seedlinglearning</p>
</body>
</html>
```